Vela Stewardship Business Card design

We need a creative business card design for our hospitality management company
We need the following information:
Our business Logo: Vela Stewardship
Name: Mara Dobrinsky
Phone number: 0458 317 642
Email: mara@velastewardship.com.au
Address: 214/53 Penrose Street, Kestrel Bay 3917
Web: www.velastewardship.com.au
I need the design to be a working file so that I can insert the names and numbers of the other staff members of our business.
The cards need to be 90 x 40mm
Thanks
Industry/Entity Type
Hospitality
Look and feel

```html
<!DOCTYPE html>
<html lang="en">
<head>
<meta charset="utf-8">
<title>Vela Stewardship Business Card</title>
<link href="https://fonts.googleapis.com/css2?family=Open+Sans:wght@400;700&display=swap" rel="stylesheet">
<style>
  :root {
    --backdrop: #3b3b3d;
    --card-light: #ffffff;
    --card-dark: #0e0e0e;
    --brand-orange: #e8921c;
    --ink: #141414;
    --paper-text: #ffffff;
    --muted: #d4d4d4;
  }
  * { margin: 0; padding: 0; box-sizing: border-box; }
  html, body {
    width: 1200px;
    height: 907px;
    overflow: hidden;
    background: var(--backdrop);
    font-family: "Open Sans", sans-serif;
  }
  .stage {
    width: 1200px;
    height: 907px;
    display: flex;
    flex-direction: column;
    align-items: center;
    justify-content: center;
    gap: 56px;
  }
  .card {
    width: 640px;
    height: 284px;
    position: relative;
    box-shadow: 0 10px 28px rgba(0,0,0,0.45);
  }
  .card-front { background: var(--card-light); color: var(--ink); }
  .card-back {
    background: var(--card-dark);
    color: var(--paper-text);
    display: flex;
    flex-direction: column;
    align-items: center;
    justify-content: center;
  }

  /* Front */
  .brand-row {
    position: absolute;
    left: 50px;
    top: 46px;
    display: flex;
    align-items: center;
    gap: 20px;
  }
  .brand-mark {
    width: 64px;
    height: 64px;
    background: var(--brand-orange);
  }
  .brand-name {
    font-weight: 700;
    font-size: 30px;
    letter-spacing: 0.5px;
    text-transform: uppercase;
    color: var(--ink);
  }
  .contact {
    position: absolute;
    left: 134px;
    top: 140px;
  }
  .contact-name {
    font-weight: 700;
    font-size: 23px;
    color: var(--brand-orange);
    margin-bottom: 8px;
  }
  .contact-line {
    font-size: 15px;
    line-height: 23px;
    color: var(--ink);
  }

  /* Back */
  .brand-mark-large {
    width: 92px;
    height: 92px;
    background: var(--brand-orange);
    margin-bottom: 20px;
  }
  .brand-name-large {
    font-weight: 700;
    font-size: 34px;
    letter-spacing: 0.5px;
    text-transform: uppercase;
    color: var(--paper-text);
  }
  .web {
    margin-top: 10px;
    font-size: 15px;
    color: var(--muted);
  }
</style>
</head>
<body>
  <main class="stage">
    <section class="card card-front">
      <div class="brand-row">
        <div class="brand-mark"></div>
        <div class="brand-name">Vela Stewardship</div>
      </div>
      <div class="contact">
        <p class="contact-name">Mara Dobrinsky</p>
        <p class="contact-line">Phone number: 0458 317 642</p>
        <p class="contact-line">Email: mara@velastewardship.com.au</p>
        <p class="contact-line">Address: 214/53 Penrose Street, Kestrel Bay 3917</p>
      </div>
    </section>

    <section class="card card-back">
      <div class="brand-mark-large"></div>
      <div class="brand-name-large">Vela Stewardship</div>
      <p class="web">www.velastewardship.com.au</p>
    </section>
  </main>
</body>
</html>
```